VoIP Postcard - New customer prospects

Need a postcard that gets our brand in front of the locals. We are an established IT company that has been in business for 20 years. We need to put a campaign in front of local businesses to let then know what we do. You can see our info at brightlinkvoice.com. We currently do not have a logo for our branded BrightlinkVoice VoIP service, which is part of Copper Harbor Networks.

Target Market(s)

Business Owners

Industry/Entity Type

Business

Colors
0355a3
3276b5
33a6d7
ec1f27
f04a50

```html
<!DOCTYPE html>
<html lang="en">
<head>
<meta charset="utf-8">
<title>Brightlink Voice Postcard</title>
<link rel="stylesheet" href="https://fonts.googleapis.com/css2?family=Hind:wght@400;500;600&family=Montserrat:wght@600;700&family=Oswald:wght@500&display=swap">
<style>
:root{
  --navy:#0355a3;
  --blue:#3276b5;
  --sky:#33a6d7;
  --red:#ec1f27;
  --red-soft:#f04a50;
  --silver:#b9bcc2;
  --page:#e6e7ea;
  --ink:#1f1f1f;
  --white:#ffffff;
}
*{margin:0;padding:0;box-sizing:border-box}
html,body{width:816px;height:1200px;overflow:hidden;background:var(--page)}
.stage{position:absolute;left:0;top:0;width:850px;height:1250px;transform:scale(.96);transform-origin:0 0;font-family:"Hind",sans-serif}
.card{position:absolute;left:56px;width:739px;background:var(--white);overflow:hidden;box-shadow:0 4px 14px rgba(0,0,0,.25)}
.card--front{top:42px;height:566px}
.card--back{top:645px;height:568px}
.card svg.art{position:absolute;left:0;top:0;width:100%;height:100%}
.abs{position:absolute}

/* front */
.company{left:46px;top:58px;display:flex;align-items:center;gap:10px;color:var(--white);font-weight:600;font-size:17px}
.company__dot{width:22px;height:22px;border-radius:50%;background:var(--red)}
.pitch{left:47px;top:170px;color:var(--white);font-size:27px;line-height:32px;font-weight:500}
.rain{left:47px;top:297px;color:var(--white);font-size:29px;font-weight:500;letter-spacing:.3px}
.rain-copy{left:47px;top:335px;color:var(--white);font-size:21px;line-height:26px;font-weight:500}
.call-tab{left:100px;top:426px;width:206px;height:29px;background:var(--red);border-radius:0 14px 0 0;color:var(--white);font-family:"Montserrat",sans-serif;font-weight:700;font-size:21px;line-height:29px;padding-left:34px}
.call-badge{left:47px;top:420px;width:70px;height:70px;border-radius:50%;background:var(--white);border:5px solid var(--red);display:flex;align-items:center;justify-content:center}
.brand{left:460px;top:30px;width:245px;color:var(--navy);font-family:"Montserrat",sans-serif;font-weight:700;font-size:22px;text-align:center;letter-spacing:.2px}
.brand-rule{left:500px;top:62px;width:165px;height:1px;background:var(--silver)}
.welcome{right:37px;top:94px;color:var(--red);font-family:"Montserrat",sans-serif;font-weight:700;font-size:29px;line-height:36px;text-align:right}
.phone-photo{left:440px;top:222px;width:250px;height:290px;border-radius:14px;background:linear-gradient(160deg,#45484e 0%,#2b2d31 55%,#1c1d20 100%);box-shadow:0 6px 14px rgba(0,0,0,.3)}
.front-phone{left:47px;top:520px;display:flex;align-items:center;gap:10px;color:var(--white);font-family:"Montserrat",sans-serif;font-weight:700;font-size:29px}
.front-web{left:407px;top:528px;display:flex;align-items:center;gap:8px;color:var(--white);font-size:21px;font-weight:500}

/* back */
.about-tab{left:0;top:18px;width:210px;height:30px;background:var(--navy);border-radius:0 16px 0 0;color:var(--white);font-size:23px;font-weight:500;line-height:32px;padding-left:33px}
.about-copy{left:33px;top:62px;width:305px;color:var(--ink);font-size:13px;line-height:15.7px}
.about-copy p{margin-bottom:12px}
.contact-tab{left:215px;top:344px;width:140px;height:38px;background:var(--red);color:var(--white);font-family:"Oswald",sans-serif;font-size:21px;line-height:34px;text-align:center;clip-path:polygon(0 0,100% 0,100% 80%,60% 80%,50% 100%,40% 80%,0 80%)}
.contact-list{left:33px;top:366px;color:var(--white);font-size:17px;line-height:22px}
.contact-list div{display:flex;align-items:center;gap:8px}
.contact-list .indent{padding-left:22px}
.contact-list .strong{font-family:"Montserrat",sans-serif;font-weight:700;font-size:14px}
.stamp{left:603px;top:35px;width:98px;height:98px;border:1px solid #9a9a9a}
.addr-line{left:463px;width:238px;height:1px;background:#9a9a9a}
</style>
</head>
<body>
<div class="stage">

  <section class="card card--front">
    <svg class="art" viewBox="0 0 739 566" aria-hidden="true">
      <defs>
        <linearGradient id="blueFade" x1="0" y1="0" x2="0" y2="1">
          <stop offset="0" stop-color="#0355a3"/>
          <stop offset=".55" stop-color="#3276b5"/>
          <stop offset="1" stop-color="#2d5f8f"/>
        </linearGradient>
        <linearGradient id="hills" x1="0" y1="0" x2="0" y2="1">
          <stop offset="0" stop-color="#ffffff"/>
          <stop offset=".3" stop-color="#d3dbe4"/>
          <stop offset="1" stop-color="#8a9bb0"/>
        </linearGradient>
      </defs>
      <rect x="370" y="170" width="369" height="396" fill="url(#hills)" role="img" aria-label="Mountain landscape photo"/>
      <path d="M0 0 H395 C450 130 470 300 445 566 H0 Z" fill="#c7cbd1"/>
      <path d="M0 0 H368 C425 130 445 300 422 566 H0 Z" fill="url(#blueFade)"/>
      <path d="M0 430 Q360 530 739 415 L739 566 L0 566 Z" fill="#d2d5da"/>
      <path d="M0 448 Q360 545 739 432 L739 566 L0 566 Z" fill="var(--white)"/>
      <path d="M0 455 Q360 560 739 440 L739 566 L0 566 Z" fill="var(--red)"/>
      <path d="M0 505 Q360 525 739 500 L739 566 L0 566 Z" fill="#d81920" opacity=".6"/>
    </svg>

    <div class="abs company"><span class="company__dot"></span>Copper Harbor Networks</div>
    <div class="abs pitch">Enjoy Peace Of Mind<br>And Relax Knowing<br>Your Phones Work For You</div>
    <div class="abs rain">RAIN OR SHINE</div>
    <div class="abs rain-copy">Brightlink Voice Service will be<br>there for you.</div>
    <div class="abs call-tab">CALL TODAY</div>
    <div class="abs call-badge">
      <svg width="36" height="36" viewBox="0 0 24 24" aria-hidden="true"><path d="M4 14v-2a8 8 0 0 1 16 0v2" fill="none" stroke="#ec1f27" stroke-width="2"/><rect x="2.5" y="12" width="4" height="6" rx="1.5" fill="#ec1f27"/><rect x="17.5" y="12" width="4" height="6" rx="1.5" fill="#ec1f27"/><path d="M19 18c0 2-2 3-5 3" fill="none" stroke="#ec1f27" stroke-width="1.6"/></svg>
    </div>

    <div class="abs brand">BRIGHTLINK VOICE</div>
    <div class="abs brand-rule"></div>
    <div class="abs welcome">Welcome to<br>Brightlink Voice</div>
    <div class="abs phone-photo" role="img" aria-label="Photo of a black VoIP desk phone with headset"></div>

    <div class="abs front-phone">
      <svg width="28" height="28" viewBox="0 0 24 24" aria-hidden="true"><circle cx="12" cy="12" r="10.5" fill="none" stroke="#fff" stroke-width="2"/><path d="M8.5 6.5l2 2.5-1.2 1.4a7 7 0 0 0 4.3 4.3l1.4-1.2 2.5 2-1.3 1.6C11.5 17 7 12.5 7 7.8z" fill="#fff"/></svg>
      0123-456-789
    </div>
    <div class="abs front-web">
      <svg width="18" height="18" viewBox="0 0 24 24" aria-hidden="true" fill="none" stroke="#fff" stroke-width="1.8"><circle cx="12" cy="12" r="10"/><ellipse cx="12" cy="12" rx="4.5" ry="10"/><path d="M2 12h20M4 7h16M4 17h16"/></svg>
      www.brightlinkvoice.com
    </div>
  </section>

  <section class="card card--back">
    <svg class="art" viewBox="0 0 739 568" aria-hidden="true">
      <defs>
        <linearGradient id="paleScene" x1="0" y1="0" x2="0" y2="1">
          <stop offset="0" stop-color="#f4f5f7"/>
          <stop offset=".5" stop-color="#efe7e3"/>
          <stop offset="1" stop-color="#f7f7f8"/>
        </linearGradient>
        <linearGradient id="contactBand" x1="0" y1="0" x2="0" y2="1">
          <stop offset="0" stop-color="#1e6bc0"/>
          <stop offset="1" stop-color="#3276b5"/>
        </linearGradient>
      </defs>
      <path d="M0 0 H360 C430 150 430 420 370 568 H0 Z" fill="url(#paleScene)" role="img" aria-label="Faded red rock landscape photo"/>
      <path d="M360 0 C430 150 430 420 370 568" fill="none" stroke="#c4c7cc" stroke-width="8"/>
      <path d="M368 0 H400 C470 160 470 410 395 568 H378 C445 410 440 160 368 0 Z" fill="var(--red)"/>
      <path d="M0 355 H385 Q395 410 375 465 H0 Z" fill="url(#contactBand)"/>
    </svg>

    <div class="abs about-tab">ABOUT US</div>
    <div class="abs about-copy">
      <p>Copper Harbor Networks Inc. has a trained and certified staff to implement, maintain, troubleshoot your network, and to address your computer repair needs. We have been meeting small to midsize businesses’ needs for over ten years and have the experience and the resources necessary to provide your business with the best possible solutions.</p>
      <p>We want to keep our clients ahead of the technology curve…why work for technology when technology can work for you? From simple print sharing to full-scale server based network solutions, we can help your company make the most of the technology available.</p>
      <p>We can come to you onsite or you can bring your PC or printer into our office for repair. We work hard to make it easy for you.</p>
    </div>

    <div class="abs contact-tab">CONTACT US</div>
    <div class="abs contact-list">
      <div><svg width="14" height="16" viewBox="0 0 24 24" aria-hidden="true" fill="none" stroke="#fff" stroke-width="2"><path d="M12 21s-7-7-7-12a7 7 0 0 1 14 0c0 5-7 12-7 12z"/><circle cx="12" cy="9" r="2.5"/></svg>Address Line 1</div>
      <div class="indent">Address Line 2</div>
      <div style="margin-top:3px"><svg width="14" height="12" viewBox="0 0 24 18" aria-hidden="true" fill="none" stroke="#fff" stroke-width="2"><rect x="1" y="1" width="22" height="16"/><path d="M1 1l11 9 11-9"/></svg>hello@brightlinkvoice.com
        <span class="strong" style="margin-left:10px;display:flex;align-items:center;gap:6px"><svg width="15" height="15" viewBox="0 0 24 24" aria-hidden="true"><circle cx="12" cy="12" r="10.5" fill="none" stroke="#fff" stroke-width="2"/><path d="M8.5 6.5l2 2.5-1.2 1.4a7 7 0 0 0 4.3 4.3l1.4-1.2 2.5 2-1.3 1.6C11.5 17 7 12.5 7 7.8z" fill="#fff"/></svg>0123-456-789</span></div>
      <div><svg width="14" height="14" viewBox="0 0 24 24" aria-hidden="true" fill="none" stroke="#fff" stroke-width="2"><circle cx="12" cy="12" r="10"/><ellipse cx="12" cy="12" rx="4.5" ry="10"/><path d="M2 12h20"/></svg>www.brightlinkvoice.com</div>
    </div>

    <div class="abs stamp"></div>
    <div class="abs addr-line" style="top:307px"></div>
    <div class="abs addr-line" style="top:354px"></div>
    <div class="abs addr-line" style="top:401px"></div>
  </section>

</div>
</body>
</html>
```